Modern luxury trendy cosmetics label

Looking for a cosmetics packaging label design. We are looking for a professionel, modern and luxury look like Lorena Vasquel, Meadowkin Apothecary, Marigold Tessin, Gavin Albert Pruke, Zuna, Orvik + Dalle, Velumi, Sleepy Walrus, the plainfold, lumiere de sable.Name of product: Nordic Tulip Mask - Needle-Free Contour Ritual Ingredients that have scientific proof of anti aging: Cherry blossom extact, collegen, hyaluronic acid, coconut oil. Color of product itself: Pastel pink. Smell: Cherry blossom. Colors of label: simple and black and white or some subtle colors.

Target Market(s)

Women, luxury market, modern women, young and old women

Industry/Entity Type

Cosmetics

Font styles to use
Sans Serif

Colors

Designer to choose colors to be used in the design.

Requirements
Must have
• A modern look, professional, cosmetics, beauty, professional market, original

```html
<!DOCTYPE html>
<html lang="en">
<head>
<meta charset="UTF-8">
<title>Orlea — Nordic Tulip Mask</title>
<link href="https://fonts.googleapis.com/css2?family=Barlow+Semi+Condensed:wght@400;500&family=Barlow:wght@300;400&display=swap" rel="stylesheet">
<style>
  :root {
    --backdrop: #f3f3f4;
    --pouch-pink: #f1ccf0;
    --pouch-pink-light: #f6daf4;
    --seal-line: rgba(120, 70, 120, 0.12);
    --ink: #141414;
    --art-pink: #e9b9e6;
  }
  html, body {
    margin: 0;
    padding: 0;
    width: 1200px;
    height: 835px;
    overflow: hidden;
    background: var(--backdrop);
  }
  h1, h2, h3, p { margin: 0; }
  .canvas {
    position: relative;
    width: 1200px;
    height: 835px;
    background: var(--backdrop);
  }
  .pouch {
    position: absolute;
    left: 437px;
    top: 41px;
    width: 380px;
    height: 680px;
    background: linear-gradient(180deg, var(--pouch-pink) 0%, var(--pouch-pink-light) 100%);
    border-radius: 14px 14px 6px 6px;
  }
  .pouch__seal {
    position: absolute;
    left: 0;
    right: 0;
    top: 70px;
    height: 1px;
    background: var(--seal-line);
  }
  .brand-name {
    position: absolute;
    left: 0;
    top: 14px;
    width: 100%;
    text-align: center;
    font-family: "Barlow Semi Condensed", sans-serif;
    font-weight: 400;
    font-size: 200px;
    line-height: 1;
    letter-spacing: -2px;
    color: var(--ink);
  }
  .product-title {
    position: absolute;
    left: 0;
    top: 221px;
    width: 100%;
    text-align: center;
    font-family: "Barlow Semi Condensed", sans-serif;
    font-weight: 500;
    font-size: 38px;
    line-height: 1;
    color: var(--ink);
  }
  .product-subtitle {
    position: absolute;
    left: 0;
    top: 263px;
    width: 100%;
    text-align: center;
    font-family: "Barlow", sans-serif;
    font-weight: 400;
    font-size: 14px;
    line-height: 1;
    color: var(--ink);
  }
  .illustration {
    position: absolute;
    left: 105px;
    top: 298px;
    width: 193px;
    height: 230px;
  }
  .scent-name {
    position: absolute;
    left: 0;
    top: 532px;
    width: 100%;
    text-align: center;
    font-family: "Barlow Semi Condensed", sans-serif;
    font-weight: 500;
    font-size: 38px;
    line-height: 1;
    color: var(--ink);
  }
  .ingredients {
    position: absolute;
    left: 30px;
    right: 30px;
    top: 586px;
    text-align: center;
    font-family: "Barlow", sans-serif;
    font-weight: 400;
    font-size: 13px;
    line-height: 18px;
    color: var(--ink);
  }
</style>
</head>
<body>
<main class="canvas">
  <section class="pouch">
    <div class="pouch__seal"></div>
    <h1 class="brand-name">orlea</h1>
    <h2 class="product-title">Nordic Tulip Mask</h2>
    <p class="product-subtitle">Needle-Free Contour Ritual</p>
    <svg class="illustration" role="img" aria-label="Line illustration of a pair of cherries on a stem with a leaf" viewBox="0 0 193 230">
      <rect x="0" y="0" width="193" height="230" rx="10" fill="var(--art-pink)"/>
    </svg>
    <h3 class="scent-name">Cherry blossom</h3>
    <p class="ingredients">Ingredients that have scientific proof of anti aging:<br>Cherry blossom extact, collegen, hyaluronic acid,<br>coconut oil.</p>
  </section>
</main>
</body>
</html>
```